Make a medical leaflet for my patients undergoing ankle blocks

I have a very boring text only leaflet I would like to turn into a professional appealing medical leaflet to give to my patients. I would like to get this onto two pages of a4 if possible and its intended for electronic distribution mainly.
This will be for patients so it must be professional.
It must also contain a copyright logo on it and my name near the start (Dr Tobias Wendell) so my colleagues can't use it easily.
Target Market(s)
Patients undergoing surgery
Industry/Entity Type
Medical
Font styles to use
Other font styles liked:
- no idea, you tell me
Requirements
Must have
- the information contained on the attachment
- look professional
- a copyright on it
Nice to have
- the ashbury clinic logo
Should not have
- Any spelling, grammatical or linguistic errors
- Any font less than size 12

```html
<!DOCTYPE html>
<html lang="en">
<head>
<meta charset="utf-8">
<title>Ankle Block – Patient Leaflet</title>
<link href="https://fonts.googleapis.com/css2?family=Montserrat:wght@500;700;800&family=Roboto:wght@400;500&display=swap" rel="stylesheet">
<style>
:root{
  --bg:#58585b;
  --paper:#ffffff;
  --blue:#1a9ad6;
  --blue-deep:#1d4f8c;
  --navy:#1a4a66;
  --panel:#3aa6dc;
  --text:#4a4a4a;
  --muted:#666;
  --band:#eef0f2;
  --num:#8ccbec;
  --rule:#9a9a9a;
}
*{box-sizing:border-box;margin:0;padding:0}
html,body{width:1200px;height:1200px;overflow:hidden;background:var(--bg)}
body{position:relative;font-family:'Roboto',sans-serif;color:var(--text)}
.page{position:absolute;background:var(--paper);overflow:hidden}
.page--front{left:67px;top:251px;width:524px;height:678px}
.page--back{left:632px;top:251px;width:516px;height:668px}
.abs{position:absolute}
.network{left:0;top:0;width:100%;height:120px;background:linear-gradient(180deg,#eef1f4 0%,#ffffff 100%)}
.author{font-family:'Montserrat',sans-serif;font-weight:700;color:var(--blue);font-size:17px;letter-spacing:.2px}
.author sup{font-size:8px}
.title-box{left:0;top:73px;width:201px;height:88px;background:var(--blue);padding:6px 0 0 28px}
.title-box h1{font-family:'Montserrat',sans-serif;font-weight:500;color:#fff;font-size:42px;line-height:38px;letter-spacing:-1px}
.partner{display:flex;align-items:center;gap:8px}
.partner-name{font-family:'Roboto',sans-serif;color:var(--blue-deep);font-size:10px;text-align:right;line-height:13px}
.partner-sub{font-size:6px}
.clinic-mark{display:flex;align-items:center;gap:4px}
.clinic-square{width:40px;height:40px;background:var(--blue-deep)}
.clinic-name{font-size:7px;color:var(--blue-deep);text-transform:uppercase;letter-spacing:1px;width:46px;line-height:9px}
.body p{font-size:10px;line-height:12.3px;margin-bottom:6px}
h2{font-family:'Montserrat',sans-serif;font-weight:800;color:var(--blue);font-size:16.5px;letter-spacing:.2px}
h3{font-family:'Montserrat',sans-serif;font-weight:800;color:var(--blue);font-size:12.5px;letter-spacing:.3px}
.benefits{list-style:none;margin-top:8px}
.benefits li{display:flex;gap:6px;font-size:10px;line-height:12.3px;margin-bottom:5px}
.benefits .n{flex:none;width:14px;height:14px;background:var(--num);color:#fff;font-size:6px;text-align:center;line-height:14px}
.benefits b{font-weight:500;color:#333}
.vrule{left:287px;top:171px;width:1px;height:450px;background:var(--rule)}
.risk{border-top:1px solid var(--rule);padding-top:6px;margin-top:6px}
.risk p,.risk li{font-size:10px;line-height:12.3px;color:var(--muted)}
.risk ul{list-style:none;padding-left:6px}
.risk ul li::before{content:"• "}
.lead{font-size:8.5px;line-height:11px;font-weight:500;color:#555;margin-top:4px;padding-bottom:4px;border-bottom:3px double var(--rule)}
.curve{left:0;bottom:0;width:100%;height:16px}
.how-head{left:28px;top:30px;background:var(--navy);color:#fff;font-family:'Montserrat',sans-serif;font-weight:800;font-size:18px;padding:2px 6px;letter-spacing:.4px}
.bullets{list-style:none}
.bullets li{position:relative;padding-left:10px;font-size:9.2px;line-height:12px;margin-bottom:4px;color:#444}
.bullets li::before{content:"";position:absolute;left:0;top:4px;width:3px;height:3px;border-radius:50%;background:var(--blue)}
.after{left:274px;top:0;width:222px;height:445px;background:var(--panel);border-radius:0 0 10px 10px;padding:28px 14px 0 15px;color:#fff}
.after h2{color:#fff;font-size:16.5px;margin-bottom:10px}
.after p{font-size:9.3px;line-height:12px;margin-bottom:6px}
.alt-band{left:0;top:463px;width:100%;height:138px;background:linear-gradient(180deg,#eceef0,#f6f7f8);padding:18px 0 0 33px;border-top:1px solid #d8d8d8;border-bottom:1px solid #d8d8d8}
.alt-band p{font-size:8.3px;line-height:10.6px;color:#555}
.alt-cols{display:flex;gap:50px;margin-top:8px}
</style>
</head>
<body>

<section class="page page--front">
  <div class="abs network" role="img" aria-label="Faint grey network pattern background"></div>
  <div class="abs author" style="left:30px;top:33px">DR. TOBIAS WENDELL<sup>®</sup></div>
  <div class="abs title-box"><h1>ANKLE<br>BLOCK</h1></div>
  <div class="abs partner" style="right:33px;top:85px">
    <div class="partner-name">Riverside Gate Hospital<br><span class="partner-sub">part of Meridian Health UK</span></div>
    <div class="clinic-square"></div>
    <div class="clinic-name">The Ashbury Clinic</div>
  </div>

  <div class="abs body" style="left:27px;top:173px;width:218px">
    <p>You are scheduled to have surgery on your foot. It is my normal practice to offer and perform (with your consent) an ankle block. This is an optional injection of numbing liquid to the nerves which supply your foot. The ankle block can be performed when you are awake, sedated or under general anaesthesia.</p>
    <p>The ankle block can be combined with a general anaesthetic and with sedation. It can also be used to allow surgery to be performed with you wide awake in certain cases.</p>
    <p>Having or not having an ankle block does not change the pre-operative fasting guidelines you have been given.</p>
    <p>There is a fee for performing an ankle block. Please consult my initial introductory email and terms of business for details.</p>
  </div>

  <div class="abs" style="left:26px;top:421px;width:240px">
    <h2>WHAT ARE THE BENEFITS</h2>
    <ol class="benefits">
      <li><span class="n">1</span><span><b>Excellent pain relief</b> - usually 10 - 14 hours (and rarely 24 - 48 hours)</span></li>
      <li><span class="n">2</span><span><b>Avoiding traditional painkillers</b> which results in less post-operative nausea and vomiting</span></li>
      <li><span class="n">3</span><span><b>The option to avoid</b> a general anaesthetic (if you wish)</span></li>
      <li><span class="n">4</span><span><b>A faster recovery</b> from the general anaesthetic</span></li>
      <li><span class="n">5</span><span><b>Certain surgery requires</b> an overnight stay in hospital without an ankle block</span></li>
    </ol>
  </div>

  <div class="abs vrule"></div>

  <div class="abs" style="left:304px;top:171px;width:192px">
    <h2>WHAT ARE THE RISKS?</h2>
    <p class="lead">As with all injections, there is the risk of bruising, bleeding and infection.</p>
    <div class="risk" style="border-top:none;margin-top:4px">
      <h3>1&nbsp; NERVE DAMAGE</h3>
      <p>Occurs 1 in 5000 nerve blocks. Creates an area of numbness or weakness/paralysis in some / all the foot. The majority of nerve injuries will heal themselves within a year. There is no treatment to fix it. If the block has not worn off after 72 hours please let me know.</p>
    </div>
    <div class="risk">
      <h3>2&nbsp; FAILURE</h3>
      <p>The success rate with ankle blocks is 98 - 99%. Some blocks will fail, partially or totally. If total failure, I will discuss repeating the block with your consent.</p>
    </div>
    <div class="risk">
      <h3>3 PAIN DURING OPERATION</h3>
      <p>If you choose to have wide awake surgery or surgery under sedation, the surgery will stop and I will discuss three options with you</p>
      <ul><li>More numbing liquid to be injected by the surgeon</li><li>More sedation / painkiller</li><li>Having a general anaesthetic</li></ul>
      <p style="margin-top:6px">If you decide to undergo surgery awake or sedated, there is a risk you will need to have a general anaesthetic if you feel pain. This is why the starvation instructions of awake surgery and general anaesthesia are the same.</p>
    </div>
  </div>

  <svg class="abs curve" viewBox="0 0 524 16" preserveAspectRatio="none"><path d="M0 16 Q262 -6 524 12 L524 16 Z" fill="#1a9ad6"/></svg>
</section>

<section class="page page--back">
  <div class="abs how-head">HOW IS IT DONE</div>
  <div class="abs" style="left:32px;top:65px;width:222px">
    <h3 style="margin-bottom:8px">IF YOU CHOOSE AWAKE SURGERY OR SURGERY WITH SEDATION</h3>
    <ul class="bullets">
      <li>The ankle block takes 5 - 10 minutes to perform and requires 4 - 5 injections</li>
      <li>Approximately 10 - 20 minutes to make your foot numb to pain</li>
      <li>I will check the ankle block is working before we start surgery using cold spray</li>
      <li>Sensations of touch, pressure, vibration and movement will still be felt</li>
      <li>I will use a screen so you can't see the surgery (unless you would like to see)</li>
      <li>Some patients bring headphones to block out the noise of the operation.</li>
    </ul>
    <h3 style="margin:22px 0 6px;font-size:11px">IF YOU CHOOSE A GENERAL ANAESTHETIC</h3>
    <ul class="bullets">
      <li>I will perform the ankle block after I start the general anaesthetic.</li>
      <li>You should wake up from your surgery with a comfortable and numb foot/feet</li>
      <li>If you wake in pain, we can repeat the ankle block or provide traditional painkillers</li>
      <li>Whatever you choose, there will be a cannula placed in your hand and heart and oxygen monitoring throughout.</li>
    </ul>
  </div>

  <div class="abs after">
    <h2>AFTER SURGERY</h2>
    <p>You will go to the recovery area and then onto the ward when you are ready. It will be difficult to walk while the block is working so physiotherapists will help you on your first walk. If you need crutches they will teach you how to use them.</p>
    <p>Your foot will be numb and so you will not feel where your foot is in relation to nearby objects. As a result, it is easy to knock your foot. Please take extra care while your foot is still numb.</p>
    <p>As the block wears off, the foot may feel slightly painful, tingly or hot. At this point you should take your painkillers I have prescribed. Depending on your medical history you will have up to three painkillers. I would suggest to start with all three. You will also have an anti-sickness prescribed if one of the painkillers (typically codeine or morphine) makes you feel sick.</p>
    <p>Occasionally (1 - 2%), pain when the block wears off will be severe. In this case contact your surgeon's secretary. We can use stronger pain medication, but there will be a charge in writing and getting the private prescription to you (please see my terms of business) via courier.</p>
  </div>

  <div class="abs alt-band">
    <h2 style="font-size:15px">THE ALTERNATIVE</h2>
    <div class="alt-cols">
      <div style="width:180px">
        <p>If you do not have an ankle block your surgery can still proceed.</p>
        <p style="margin-top:5px">Post-operative pain can be managed with traditional painkillers.</p>
      </div>
      <div style="width:200px"><p>However, you are more likely to need an overnight stay or feel sick after the anaesthetic.</p></div>
    </div>
    <p style="margin-top:10px">If you have any further questions about an ankle block I will see you the day of your surgery.</p>
    <p style="margin-top:5px">Alternatively, you can request the following optional services (as mentioned in my terms of business).</p>
  </div>

  <div class="abs author" style="left:40px;top:631px">DR. TOBIAS WENDELL<sup>®</sup></div>
  <div class="abs partner" style="right:30px;top:617px">
    <div class="partner-name" style="font-size:8.5px;line-height:11px">Riverside Gate Hospital<br><span class="partner-sub">part of Meridian Health UK</span></div>
    <div class="clinic-square" style="width:38px;height:38px"></div>
    <div class="clinic-name" style="width:44px">The Ashbury Clinic</div>
  </div>
</section>

</body>
</html>
```